Business card for a new cabinet shop company named Torvane Cabinets for high end cabinets

Design a business card, thinking dark rich green with colours to speak of high end luxury ie; cream, gold, black possibly

Miles Harwick
Director Craftsman
Email: info@torvanecabinets.com.au
Instagram : @torvane.cabinets

```html
<!DOCTYPE html>
<html lang="en">
<head>
<meta charset="utf-8">
<title>Torvane Cabinets — Business Card</title>
<link href="https://fonts.googleapis.com/css2?family=Montserrat:wght@400;500;800&display=swap" rel="stylesheet">
<style>
  :root {
    --backdrop: #2b2b2c;
    --card: #151515;
    --gold: #c7a865;
    --white: #f4f2ee;
    --sheen: rgba(255,255,255,.07);
  }
  * { box-sizing: border-box; margin: 0; padding: 0; }
  html, body { width: 1200px; height: 694px; overflow: hidden; }
  body {
    background: var(--backdrop);
    font-family: "Montserrat", sans-serif;
    display: flex;
    align-items: center;
    justify-content: center;
    gap: 48px;
  }
  .card {
    position: relative;
    width: 520px;
    height: 300px;
    border-radius: 18px;
    background: var(--card);
    overflow: hidden;
    box-shadow: 0 18px 40px rgba(0,0,0,.45);
  }
  .card__pattern {
    position: absolute;
    inset: 0;
    background:
      linear-gradient(115deg, transparent 0%, var(--sheen) 22%, transparent 38%, transparent 62%, rgba(255,255,255,.04) 78%, transparent 90%),
      radial-gradient(ellipse at 25% 60%, #2a2a2a 0%, #1a1a1a 50%, #111 100%);
  }
  .card--back::after {
    content: "";
    position: absolute;
    inset: 0;
    background: linear-gradient(115deg, transparent 55%, rgba(255,255,255,.05) 70%, transparent 82%);
    pointer-events: none;
  }
  .brand {
    position: relative;
    display: flex;
    align-items: center;
    gap: 18px;
  }
  .card--front .brand { height: 100%; justify-content: center; }
  .brand__dot {
    width: 16px;
    height: 16px;
    border-radius: 50%;
    background: var(--gold);
    flex: 0 0 auto;
  }
  .brand__name {
    display: flex;
    flex-direction: column;
    color: var(--gold);
    font-weight: 500;
    line-height: 1;
  }
  .brand__word { font-size: 56px; letter-spacing: .01em; }
  .brand__sub {
    font-size: 21px;
    letter-spacing: .42em;
    margin-top: 8px;
    padding-left: 3px;
  }
  .card--back .brand { gap: 10px; flex: 0 0 auto; }
  .card--back .brand__dot { width: 10px; height: 10px; }
  .card--back .brand__word { font-size: 30px; }
  .card--back .brand__sub { font-size: 11.5px; margin-top: 5px; padding-left: 2px; }
  .back-layout {
    position: relative;
    height: 100%;
    display: flex;
    align-items: center;
    padding: 0 26px 0 30px;
  }
  .divider {
    flex: 0 0 2px;
    width: 2px;
    height: 150px;
    background: var(--gold);
    margin: 0 20px;
  }
  .contact { flex: 1 1 auto; min-width: 0; }
  .contact__name {
    font-weight: 800;
    color: var(--gold);
    font-size: 21px;
    line-height: 1.1;
  }
  .contact__role {
    color: var(--white);
    font-size: 13px;
    margin: 3px 0 16px;
  }
  .contact__list { list-style: none; }
  .contact__item {
    display: flex;
    align-items: center;
    gap: 7px;
    color: var(--white);
    font-size: 11.5px;
    line-height: 1;
    margin-bottom: 10px;
    white-space: nowrap;
  }
  .contact__icon { width: 12px; height: 12px; flex: 0 0 12px; }
</style>
</head>
<body>

  <section class="card card--front">
    <div class="card__pattern" role="img" aria-label="Faint repeating embossed monogram pattern across the card"></div>
    <div class="brand">
      <span class="brand__dot"></span>
      <span class="brand__name">
        <span class="brand__word">Torvane</span>
        <span class="brand__sub">CABINETS</span>
      </span>
    </div>
  </section>

  <section class="card card--back">
    <div class="back-layout">
      <div class="brand">
        <span class="brand__dot"></span>
        <span class="brand__name">
          <span class="brand__word">Torvane</span>
          <span class="brand__sub">CABINETS</span>
        </span>
      </div>
      <div class="divider"></div>
      <div class="contact">
        <p class="contact__name">Miles Harwick</p>
        <p class="contact__role">Director Craftsman</p>
        <ul class="contact__list">
          <li class="contact__item">
            <svg class="contact__icon" viewBox="0 0 16 16"><rect x="1" y="3" width="14" height="10" rx="1" fill="var(--white)"/><path d="M1.5 4 8 9l6.5-5" stroke="var(--card)" stroke-width="1.4" fill="none"/></svg>
            info@torvanecabinets.com.au
          </li>
          <li class="contact__item">
            <svg class="contact__icon" viewBox="0 0 16 16"><circle cx="8" cy="8" r="6.5" fill="none" stroke="var(--white)" stroke-width="1.4"/><ellipse cx="8" cy="8" rx="2.6" ry="6.5" fill="none" stroke="var(--white)" stroke-width="1.2"/><path d="M1.5 8h13" stroke="var(--white)" stroke-width="1.2"/></svg>
            torvanecabinets.com.au
          </li>
          <li class="contact__item">
            <svg class="contact__icon" viewBox="0 0 16 16"><circle cx="8" cy="8" r="6" fill="none" stroke="var(--white)" stroke-width="1.4"/></svg>
            @torvane.cabinets
          </li>
        </ul>
      </div>
    </div>
  </section>

</body>
</html>
```